"Lanternfold": Dorian Vell's new EP

Esteemed Designers, thanks for considering my project! I am producing a 4-song EP entitled "Lanternfold" The CD sleeve will be a simple two sided design with designed image of a lanternfold like the attached, though it does not need to be photorealistic. It could be a highly stylized version. I do think it needs to be square however since CD covers are square. The back and front should be the back and front of the lanternfold. Could be color (muted!) or grayscale. This is my website to give you a feel of my previous work and aesthetic: dorianvell.net I am attaching a zipped file of the CD sleeve template I plan to use for manufacturing.

Target Market(s)

music lovers, previous fans of mine, and hopefully new ones

Industry/Entity Type

Music Download

Colors

Designer to choose colors to be used in the design.

Requirements
Must have
• Simplicity, an iconic feel, strength of conviction in the lines. Grace and Economy.
• The front cover will say: "Dorian Vell" and "Lanternfold" though how you present text is of course up to you.
• The back cover will list the 4 songs:
• 1. The Hour Of My Flight (3:25)
• 2. Take The Coat Or Take The Key (3:39)
• 3. Pull Me Near (3:51)
• 4. Slipping East (3:10)
• and have a link to my website: www.dorianvell.net
• The CD itself could look like a sheet of a paper (hence the "lanternfold"). It would have the song titles, my website, as well as the copyright and phonorecord symbols ("c" and "p" within circles ) "2018" and say "dorian vell. unauthorized duplication prohibited"

```html
<!DOCTYPE html>
<html lang="en">
<head>
<meta charset="utf-8">
<title>Lanternfold — Dorian Vell — Back Cover</title>
<link rel="stylesheet" href="https://fonts.googleapis.com/css2?family=Amatic+SC:wght@400;700&family=Arimo:wght@400&display=swap">
<style>
  :root {
    --leather-light: #c4561f;
    --leather-mid: #aa4117;
    --leather-dark: #8a2f0e;
    --stitch: #d08a48;
    --ink: #fcc774;
    --ink-soft: #f3b866;
    --fine-print: #ffffff;
  }
  html, body {
    margin: 0;
    padding: 0;
    width: 1171px;
    height: 1200px;
    overflow: hidden;
    background: var(--leather-mid);
  }
  .back-cover {
    position: relative;
    width: 1171px;
    height: 1200px;
    overflow: hidden;
    background:
      radial-gradient(ellipse at 55% 45%, var(--leather-mid) 0%, transparent 65%),
      radial-gradient(ellipse at 15% 85%, var(--leather-light) 0%, transparent 45%),
      linear-gradient(160deg, var(--leather-light) 0%, var(--leather-mid) 45%, var(--leather-dark) 100%);
  }
  .leather-texture {
    position: absolute;
    inset: 0;
  }
  .stitching {
    position: absolute;
    inset: 0;
  }
  .tracklist {
    position: absolute;
    top: 316px;
    left: 0;
    width: 100%;
    margin: 0;
    padding: 0;
    list-style: none;
    text-align: center;
    font-family: "Amatic SC", "Arial Narrow", sans-serif;
    color: var(--ink);
    text-shadow: 0 2px 4px rgba(80, 20, 0, 0.35);
  }
  .track {
    height: 106px;
    line-height: 106px;
    white-space: nowrap;
  }
  .track-title {
    font-weight: 700;
    font-size: 92px;
  }
  .track-length {
    font-weight: 400;
    font-size: 66px;
    color: var(--ink-soft);
    opacity: 0.9;
  }
  .website {
    position: absolute;
    top: 872px;
    left: 0;
    width: 100%;
    text-align: center;
    font-family: "Amatic SC", "Arial Narrow", sans-serif;
    font-weight: 700;
    font-size: 44px;
    color: var(--fine-print);
    letter-spacing: 0.5px;
    margin: 0;
  }
  .legal {
    position: absolute;
    top: 966px;
    left: 0;
    width: 100%;
    text-align: center;
    font-family: "Arimo", Arial, sans-serif;
    font-size: 14px;
    color: var(--fine-print);
    margin: 0;
  }
</style>
</head>
<body>
<main class="back-cover">
  <div class="leather-texture" role="img" aria-label="Tan leather surface texture"></div>

  <svg class="stitching" width="1171" height="1200" viewBox="0 0 1171 1200" aria-hidden="true">
    <g stroke="var(--stitch)" stroke-width="2.5" stroke-dasharray="7 5" stroke-linecap="round" fill="none" opacity="0.85">
      <line x1="0" y1="52" x2="1171" y2="52"/>
      <line x1="0" y1="1148" x2="1171" y2="1148"/>
      <line x1="86" y1="0" x2="86" y2="1200"/>
      <line x1="1102" y1="0" x2="1102" y2="1200"/>
    </g>
  </svg>

  <ol class="tracklist">
    <li class="track"><span class="track-title">- 1. The Hour Of My Flight</span> <span class="track-length">(3:25)</span></li>
    <li class="track"><span class="track-title">- 2. Take The Coat Or Take The Key</span> <span class="track-length">(3:39)</span></li>
    <li class="track"><span class="track-title">- 3. Pull Me Near</span> <span class="track-length">(3:51)</span></li>
    <li class="track"><span class="track-title">- 4. Slipping East</span> <span class="track-length">(3:10)</span></li>
  </ol>

  <p class="website">www.dorianvell.net</p>

  <p class="legal">℗ &amp; ©&nbsp; 2018 DORIAN VELL. UNAUTHORIZED DUPLICATION PROHIBITED</p>
</main>
</body>
</html>
```